Veltrano - Mechanic/Collision Center Business Card

We're looking for a business card design for our mechanic/ collision repair shop.

Can be with colours or monochromatic.

See the attached files.

Many thanks

```html
<!DOCTYPE html>
<html lang="en">
<head>
<meta charset="utf-8">
<title>Veltrano – Business Card</title>
<link href="https://fonts.googleapis.com/css2?family=Arimo:wght@400;700&display=swap" rel="stylesheet">
<style>
  :root {
    --stage: #d9d9db;
    --card: #ffffff;
    --ink: #111111;
    --ink-soft: #333333;
    --accent: #3aa3e3;
    --bar: #5e6266;
    --bar-edge: #2c2f31;
    --ghost: #e6e7e9;
    --muted: #cfd3d6;
  }
  * { margin: 0; padding: 0; box-sizing: border-box; }
  html, body { width: 1200px; height: 807px; overflow: hidden; }
  body {
    background: var(--stage);
    font-family: "Arimo", Arial, sans-serif;
    color: var(--ink);
    display: flex;
    align-items: center;
    justify-content: center;
    gap: 40px;
  }
  .card {
    position: relative;
    width: 540px;
    height: 310px;
    background: var(--card);
    border-radius: 26px;
    overflow: hidden;
  }

  /* Front */
  .brand {
    position: absolute;
    display: flex;
    align-items: center;
    gap: 10px;
  }
  .brand-dot {
    width: 30px; height: 30px;
    border-radius: 50%;
    background: var(--accent);
  }
  .brand-name {
    font-weight: 700;
    font-size: 36px;
    letter-spacing: 1px;
    color: var(--ink);
  }
  .front .brand { left: 36px; bottom: 48px; }

  .contact {
    position: absolute;
    left: 270px;
    top: 44px;
  }
  .company { font-weight: 700; font-size: 19px; }
  .role { font-weight: 700; font-size: 12px; color: var(--ink-soft); margin-top: 2px; }
  .lines { list-style: none; margin-top: 18px; }
  .lines li {
    display: flex; align-items: center; gap: 8px;
    font-size: 13px; margin-bottom: 9px;
  }
  .lines li.address { font-size: 16px; }
  .icon { width: 14px; height: 14px; flex: none; }

  /* Back */
  .ghost-name {
    position: absolute;
    left: 26px; top: 30px;
    font-weight: 700;
    font-size: 78px;
    letter-spacing: 2px;
    color: var(--ghost);
  }
  .back .brand { left: 120px; top: 110px; }
  .manager-bar {
    position: absolute;
    left: 14px; right: 14px; bottom: 14px;
    height: 38px;
    background: var(--bar);
    border: 3px solid var(--bar-edge);
    border-radius: 10px;
    display: flex; align-items: center;
    padding: 0 18px;
    gap: 14px;
    font-size: 15px;
  }
  .manager-name { color: var(--accent); font-size: 18px; }
  .manager-role { color: var(--muted); }
  .manager-phone { margin-left: auto; color: var(--accent); display: flex; align-items: center; gap: 8px; }
</style>
</head>
<body>
  <section class="card front">
    <div class="contact">
      <p class="company">Veltrano, LDA</p>
      <p class="role">founder &amp; CEO</p>
      <ul class="lines">
        <li class="address">
          <svg class="icon" viewBox="0 0 14 14"><path d="M7 0a5 5 0 0 0-5 5c0 3.5 5 9 5 9s5-5.5 5-9a5 5 0 0 0-5-5z" fill="#111"/><circle cx="7" cy="5" r="2" fill="#fff"/></svg>
          Rua das Oficinas,42
        </li>
        <li>
          <svg class="icon" viewBox="0 0 14 14"><circle cx="7" cy="7" r="6" fill="none" stroke="#3aa3e3" stroke-width="1.6"/><path d="M1 7h12M7 1v12" stroke="#3aa3e3" stroke-width="1.2"/></svg>
          1800-214 Lisboa
        </li>
        <li>
          <svg class="icon" viewBox="0 0 14 14"><circle cx="7" cy="7" r="7" fill="#111"/><path d="M4.5 3.5l1.5 1.5-1 1.2a5 5 0 0 0 2.8 2.8l1.2-1 1.5 1.5-1 1.1c-2.8 0-5.6-2.8-5.6-5.6z" fill="#fff"/></svg>
          +351210004512
        </li>
        <li>
          <svg class="icon" viewBox="0 0 14 14"><circle cx="7" cy="7" r="7" fill="#111"/><rect x="3.5" y="4.5" width="7" height="5" fill="#fff"/><path d="M3.5 4.5L7 7.3l3.5-2.8" fill="none" stroke="#111" stroke-width="0.8"/></svg>
          veltrano.office@mailbox.pt
        </li>
        <li>
          <svg class="icon" viewBox="0 0 14 14"><circle cx="7" cy="7" r="7" fill="#111"/></svg>
          www.veltrano-auto.pt
        </li>
      </ul>
    </div>
    <div class="brand">
      <span class="brand-dot"></span>
      <span class="brand-name">VELTRANO</span>
    </div>
  </section>

  <section class="card back">
    <p class="ghost-name" aria-hidden="true">VELTRANO</p>
    <div class="brand">
      <span class="brand-dot"></span>
      <span class="brand-name">VELTRANO</span>
    </div>
    <div class="manager-bar">
      <span class="manager-name">Mauro Vidal:</span>
      <span class="manager-role">info of manager</span>
      <span class="manager-phone">
        <svg class="icon" viewBox="0 0 14 14"><circle cx="7" cy="7" r="7" fill="#3aa3e3"/><path d="M4.5 3.5l1.5 1.5-1 1.2a5 5 0 0 0 2.8 2.8l1.2-1 1.5 1.5-1 1.1c-2.8 0-5.6-2.8-5.6-5.6z" fill="#5e6266"/></svg>
        +351920007714
      </span>
    </div>
  </section>
</body>
</html>
```